PLOVEN Business Card

Coastal Build Additions and Refits. I need a business card designed for this new high end renovation business. I would like the logo centered on the back side with the ABN (37 915 402 176) on the bottom right hand corner.

I would like the following information placed on the other side along with some customized pattern or design.

Derek Collwood
Director
Phone: 1300 480 957
Fax: (02) 8145 9021
Website: www.plovenbuilders.com.au
Email: d.collwood@plovenbuilders.com.au
PO Box 87,
Kelvinbrook NSW 2069

(FB Logo) PLOVEN - Coastal Build Additions and Refits

The final design should communicate professionalism and trust.

Back side background colour: white
Front side: Undecided

```html
<!DOCTYPE html>
<html lang="en">
<head>
<meta charset="UTF-8">
<title>PLOVEN Business Card</title>
<link href="https://fonts.googleapis.com/css2?family=Arimo:wght@400;700&family=Cinzel:wght@400;600&display=swap" rel="stylesheet">
<style>
  :root {
    --stage: #2b2b2b;
    --card-white: #ffffff;
    --card-shade: #eceef0;
    --brand-blue: #0f4f8f;
    --brand-blue-deep: #0a3c70;
    --ink: #23272b;
    --rail: #3a3d40;
    --rail-icon: #d7d9db;
    --text-light: #ffffff;
    --text-soft: #dfe7f0;
  }
  * { box-sizing: border-box; margin: 0; padding: 0; }
  html, body {
    width: 1200px; height: 900px; overflow: hidden;
    background: var(--stage);
  }
  .stage {
    position: relative; width: 1200px; height: 900px;
    display: flex; flex-direction: column; align-items: center; justify-content: center; gap: 56px;
  }
  .card {
    position: relative; width: 560px; height: 340px; overflow: hidden;
    background: linear-gradient(180deg, var(--card-white) 0%, var(--card-shade) 100%);
    box-shadow: 0 10px 28px rgba(0,0,0,.55);
  }
  .brand {
    position: absolute; left: 0; right: 0; text-align: center;
    font-family: "Cinzel", serif;
  }
  .brand-name {
    display: block; font-weight: 600; font-size: 58px; letter-spacing: 4px;
    color: var(--brand-blue); line-height: 1;
  }
  .brand-tagline {
    display: flex; align-items: center; justify-content: center; gap: 10px;
    margin-top: 6px; font-size: 15px; font-weight: 600; letter-spacing: 1px;
    color: var(--brand-blue); text-transform: uppercase;
  }
  .brand-tagline::before, .brand-tagline::after {
    content: ""; width: 40px; height: 2px; background: var(--brand-blue);
  }
  /* back side */
  .card--back .brand { top: 108px; }
  .card--back .abn-strip { position: absolute; right: 0; bottom: 0; }
  .abn-text {
    position: absolute; right: 14px; bottom: 9px;
    font-family: "Arimo", sans-serif; font-weight: 700; font-size: 14px;
    color: var(--text-light); letter-spacing: .3px;
  }
  /* front side */
  .card--front .brand { top: 30px; }
  .card--front .brand-name { font-size: 50px; }
  .card--front .brand-tagline { font-size: 13px; }
  .contact-band {
    position: absolute; left: 0; right: 0; bottom: 0; height: 190px;
    background: linear-gradient(135deg, var(--brand-blue-deep) 0%, var(--brand-blue) 100%);
  }
  .icon-rail {
    position: absolute; left: 0; top: 34px; bottom: 0; width: 30px;
    background: var(--rail);
    display: flex; flex-direction: column; align-items: center; padding-top: 8px; gap: 6px;
  }
  .icon-rail svg { width: 14px; height: 16px; fill: var(--rail-icon); }
  .contact-list {
    position: absolute; left: 42px; top: 36px; list-style: none;
    font-family: "Arimo", sans-serif; font-size: 15px; line-height: 22px;
    color: var(--text-light);
  }
  .divider {
    position: absolute; left: 370px; top: 20px; width: 2px; height: 120px;
    background: var(--text-soft); opacity: .8;
  }
  .person {
    position: absolute; left: 388px; top: 24px;
    font-family: "Arimo", sans-serif; color: var(--text-light);
  }
  .person-name { font-weight: 700; font-size: 19px; }
  .person-role { font-size: 13px; margin-top: 3px; color: var(--text-soft); }
</style>
</head>
<body>
<main class="stage">

  <section class="card card--back" aria-label="Back side">
    <div class="brand">
      <span class="brand-name">PLOVEN</span>
      <span class="brand-tagline">Coastal Build Additions and Refits</span>
    </div>
    <svg class="abn-strip" width="260" height="60" viewBox="0 0 260 60" aria-hidden="true">
      <polygon points="40,0 260,0 260,60 0,60" fill="var(--brand-blue)"/>
    </svg>
    <span class="abn-text">ABN (37 915 402 176)</span>
  </section>

  <section class="card card--front" aria-label="Front side">
    <div class="brand">
      <span class="brand-name">PLOVEN</span>
      <span class="brand-tagline">Coastal Build Additions and Refits</span>
    </div>
    <div class="contact-band">
      <div class="icon-rail" aria-hidden="true">
        <svg viewBox="0 0 16 16"><path d="M3 3c2-2 3-2 4 0l1 2-2 2c1 2 2 3 4 4l2-2 2 1c2 1 2 2 0 4-3 2-13-8-11-11z"/></svg>
        <svg viewBox="0 0 16 16"><rect x="4" y="1" width="8" height="5"/><rect x="1" y="6" width="14" height="8" rx="1"/></svg>
        <svg viewBox="0 0 16 16"><circle cx="8" cy="8" r="6.5" fill="none" stroke="var(--rail-icon)" stroke-width="1.5"/><path d="M1.5 8h13M8 1.5c-3 3-3 10 0 13M8 1.5c3 3 3 10 0 13" fill="none" stroke="var(--rail-icon)" stroke-width="1.2"/></svg>
        <svg viewBox="0 0 16 16"><rect x="1" y="3" width="14" height="10"/><path d="M1 3l7 6 7-6" fill="none" stroke="var(--rail)" stroke-width="1.3"/></svg>
        <svg viewBox="0 0 16 16"><path d="M8 15C4 10 3 8 3 6a5 5 0 0 1 10 0c0 2-1 4-5 9z"/><circle cx="8" cy="6" r="2" fill="var(--rail)"/></svg>
        <svg viewBox="0 0 16 16"><circle cx="8" cy="8" r="5.5"/></svg>
      </div>
      <ul class="contact-list">
        <li>1300 480 957</li>
        <li>(02) 8145 9021</li>
        <li>www.plovenbuilders.com.au</li>
        <li>d.collwood@plovenbuilders.com.au</li>
        <li>PO Box 87, Kelvinbrook NSW 2069</li>
        <li>www.kinlinkr.com/coastalrefits1</li>
      </ul>
      <div class="divider"></div>
      <div class="person">
        <p class="person-name">Derek Collwood</p>
        <p class="person-role">Director</p>
      </div>
    </div>
  </section>

</main>
</body>
</html>
```